BrightLoop Kiosk Business Card Design Project

BrightLoop Kiosk requires a business card design. We hire PhotoBooths to events such as Birthday Parties, Hens and Bucks Night, Anniversaries, Corporate Functions
, Engagements, Theme Nights, Presentation Night etc.
Business Card needs to look Modern, Professional And Catchy.
Updates

Hello Thankyou for all of your great designs, contact information will be provided shortly. We are considering the front of the card to be white themed and the back of the card to be black themed. And all social media colours to be their original colour. Thankyou

Hello everyone, Here are the contact details: Martin Colby - Manager Mobile number - 0491738205 Website - www.brightloopkiosk.example Email - admin@brightloopkiosk.example And if you can add the word "weddings" in the "We cater For" section would be good. Thankyou

Target Market(s)

Birthday Parties
Hens and Bucks Night
Weddings
Corporate Functions
Engagements
Theme Nights
Presentation Night
School Functions

Industry/Entity Type

Events

Requirements
Must have
• Must Match Logo
Must Have www.brightloopkiosk.example

On Back of card must have social media icons Kinfold, Chirpline, Vidstream, Linkin and

We Cater For:

Birthday Parties
Hens and Bucks Night
Anniversaries
Corporate Functions
Engagements
Theme Nights
Presentation Night
School Functions
And more.....

```html
<!DOCTYPE html>
<html lang="en">
<head>
<meta charset="utf-8">
<title>BrightLoop Kiosk – Business Cards</title>
<link rel="stylesheet" href="https://fonts.googleapis.com/css2?family=Source+Sans+3:wght@400;600;700&display=swap">
<style>
  :root {
    --bg: #e9e6e2;
    --ink: #111214;
    --paper: #ffffff;
    --accent: #29a8dc;
    --muted: #555a60;
    --light: #f4f4f4;
    --net-a: #3b5998;
    --net-b: #2aa3e0;
    --net-c: #d42a20;
    --net-d: #1a7ab8;
  }
  * { box-sizing: border-box; margin: 0; padding: 0; }
  html, body { width: 1200px; height: 900px; overflow: hidden; }
  body {
    background: var(--bg);
    font-family: "Source Sans 3", Arial, sans-serif;
    position: relative;
  }
  .card {
    position: absolute;
    width: 630px;
    height: 360px;
    border-radius: 4px;
    overflow: hidden;
    box-shadow: 0 10px 28px rgba(0,0,0,.22);
  }
  /* Back of card */
  .card--back { left: 200px; top: 50px; background: var(--ink); color: var(--light); }
  .brand {
    display: flex; align-items: center; gap: 14px;
    font-weight: 600; text-transform: uppercase; letter-spacing: 3px;
  }
  .brand__dot { width: 34px; height: 34px; border-radius: 50%; background: var(--accent); flex: none; }
  .card--back .brand { position: absolute; left: 60px; top: 52px; font-size: 34px; color: var(--paper); }
  .networks {
    position: absolute; left: 60px; top: 150px; right: 40px;
    display: flex; justify-content: space-between; list-style: none;
  }
  .network { display: flex; align-items: center; gap: 8px; font-size: 15px; color: var(--paper); }
  .network__square { width: 26px; height: 26px; border-radius: 3px; }
  .network--a .network__square { background: var(--net-a); }
  .network--b .network__square { background: var(--net-b); }
  .network--c .network__square { background: var(--net-c); }
  .network--d .network__square { background: var(--net-d); }
  .services {
    position: absolute; left: 60px; right: 50px; top: 222px;
    font-size: 19px; line-height: 1.4; color: var(--paper);
  }
  /* Front of card */
  .card--front { left: 370px; top: 480px; background: var(--paper); color: var(--ink); }
  .card--front .brand { position: absolute; left: 56px; top: 42px; font-size: 36px; color: var(--ink); }
  .swoosh { position: absolute; inset: 0; }
  .person { position: absolute; left: 44px; top: 150px; }
  .person__name { font-size: 30px; font-weight: 700; line-height: 1; }
  .person__role { font-size: 16px; color: var(--muted); margin-top: 2px; }
  .contacts {
    position: absolute; right: 22px; bottom: 30px;
    list-style: none; text-align: right; color: var(--paper); font-size: 18px; line-height: 1.55;
  }
  .contacts li { display: flex; justify-content: flex-end; align-items: center; gap: 12px; }
  .contacts svg { width: 14px; height: 14px; flex: none; }
</style>
</head>
<body>

<section class="card card--back" aria-label="Back of card">
  <div class="brand"><span class="brand__dot"></span>BrightLoop Kiosk</div>
  <ul class="networks">
    <li class="network network--a"><span class="network__square"></span>Kinfold</li>
    <li class="network network--b"><span class="network__square"></span>Chirpline</li>
    <li class="network network--c"><span class="network__square"></span>Vidstream</li>
    <li class="network network--d"><span class="network__square"></span>Linkwork</li>
  </ul>
  <p class="services">Birthday Parties, Hens and Bucks Night, Anniversaries, Corporate Functions, Engagements, Theme Nights, Presentation Night, School Functions, And more.....</p>
</section>

<section class="card card--front" aria-label="Front of card">
  <svg class="swoosh" viewBox="0 0 630 360" preserveAspectRatio="none" aria-hidden="true">
    <path d="M0,262 C170,240 320,188 450,160 C540,142 600,136 630,137 L630,150 C570,152 480,170 400,196 C260,246 120,282 0,290 Z" fill="var(--accent)"/>
    <path d="M0,300 C160,290 300,250 420,212 C520,182 590,168 630,165 L630,360 L0,360 Z" fill="var(--ink)"/>
    <path d="M30,322 C170,306 300,270 420,236 C500,214 570,200 630,196" fill="none" stroke="var(--paper)" stroke-width="2"/>
  </svg>
  <div class="brand"><span class="brand__dot"></span>BrightLoop Kiosk</div>
  <div class="person">
    <p class="person__name">Martin Colby</p>
    <p class="person__role">Manager</p>
  </div>
  <ul class="contacts">
    <li>0491738205
      <svg viewBox="0 0 14 14"><rect x="3.5" y="1" width="7" height="12" rx="1.5" fill="none" stroke="var(--accent)" stroke-width="1.5"/></svg></li>
    <li>admin@brightloopkiosk.example
      <svg viewBox="0 0 14 14"><rect x="1" y="3" width="12" height="8" fill="var(--accent)"/><path d="M1,3 L7,8 L13,3" fill="none" stroke="var(--ink)" stroke-width="1"/></svg></li>
    <li>www.brightloopkiosk.example
      <svg viewBox="0 0 14 14"><circle cx="7" cy="7" r="5.5" fill="none" stroke="var(--accent)" stroke-width="1.5"/><path d="M1.5,7 H12.5 M7,1.5 C4,5 4,9 7,12.5 M7,1.5 C10,5 10,9 7,12.5" fill="none" stroke="var(--accent)" stroke-width="1"/></svg></li>
  </ul>
</section>

</body>
</html>
```